National Dance Competition Needs a Program Cover Design

We need a program cover design for our 2017 season programs. Program size is standard 8.5" x 11", full color. The only required elements to include in the design are the Stellar Step Showcase logo (see uploaded file), and the copy: "2017 Regional Competition" and "20th Anniversary Season". All other design elements are per the creative mind of the designer. Logo can be "embellished" if that's the direction the design leads. This is a children's dance competition (ages 5-19) so design should be colorful, fun, and exciting. The winning design will likely be the springboard to other projects including designs for awards plaques, trophy mylars, and program ads. We are looking to establish an ongoing relationship with a designer. For more information about us go to www.stellarstepshowcase.example.

Target Market(s)

Dancers ages 5-19, their parents and dance instructors

Requirements
Must have
• See project description above
Should not have
• Do not fall into the mindset that dance is Ballet only. Our kids also compete in Jazz, Tap, Lyrical, Contemporary, Hip Hop and many other styles.

```html
<!DOCTYPE html>
<html lang="en">
<head>
<meta charset="utf-8">
<title>Stellar Step Showcase – 2017 Regional Competition Program Cover</title>
<link href="https://fonts.googleapis.com/css2?family=Great+Vibes&display=swap" rel="stylesheet">
<style>
  :root {
    --sky-top: #79c6cb;
    --sky-bottom: #e6f4f5;
    --ray: #5b6fb6;
    --ray-deep: #4a3d9a;
    --brand-teal: #0fa7b8;
    --ink: #0c0c12;
    --halo: #ffffff;
    --crowd-top: rgba(74, 61, 154, 0);
    --crowd-mid: #4a3d9a;
    --crowd-base: #0a0a10;
  }
  html, body {
    margin: 0;
    padding: 0;
    overflow: hidden;
    background: #ffffff;
  }
  .cover {
    position: relative;
    width: 927px;
    height: 1200px;
    overflow: hidden;
    background: linear-gradient(180deg, var(--sky-top) 0%, #a9d9dc 55%, var(--sky-bottom) 100%);
    font-family: "Great Vibes", cursive;
  }
  .sunburst {
    position: absolute;
    inset: 0;
    width: 927px;
    height: 1200px;
  }
  .sunburst polygon { fill: var(--ray); opacity: 0.92; }
  .brand {
    position: absolute;
    top: 70px;
    left: 0;
    width: 927px;
    display: flex;
    align-items: center;
    justify-content: center;
    gap: 22px;
  }
  .brand-mark {
    width: 46px;
    height: 46px;
    border-radius: 50%;
    background: var(--brand-teal);
    flex: none;
  }
  .brand-name {
    margin: 0;
    color: var(--brand-teal);
    font-family: "Great Vibes", cursive;
    font-weight: 400;
    font-size: 104px;
    line-height: 1;
    text-align: center;
  }
  .headline {
    position: absolute;
    left: 0;
    width: 927px;
    margin: 0;
    text-align: center;
    color: var(--ink);
    font-weight: 400;
    line-height: 1;
    text-shadow:
      2px 0 0 var(--halo), -2px 0 0 var(--halo),
      0 2px 0 var(--halo), 0 -2px 0 var(--halo),
      1.5px 1.5px 0 var(--halo), -1.5px -1.5px 0 var(--halo),
      1.5px -1.5px 0 var(--halo), -1.5px 1.5px 0 var(--halo);
  }
  .headline-year { top: 375px; font-size: 130px; }
  .headline-event { top: 540px; font-size: 135px; }
  .headline-season { top: 755px; font-size: 86px; }
  .crowd {
    position: absolute;
    left: 0;
    bottom: 0;
    width: 927px;
    height: 330px;
    background: linear-gradient(180deg, var(--crowd-top) 0%, var(--crowd-mid) 35%, #1c1740 65%, var(--crowd-base) 100%);
  }
</style>
</head>
<body>
  <main class="cover">
    <svg class="sunburst" viewBox="0 0 927 1200" aria-hidden="true">
      <polygon points="464,1230 0,-10 70,-10"/>
      <polygon points="464,1230 120,-10 190,-10"/>
      <polygon points="464,1230 440,-10 525,-10"/>
      <polygon points="464,1230 725,-10 805,-10"/>
      <polygon points="464,1230 -10,480 -10,640"/>
      <polygon points="464,1230 937,430 937,590"/>
      <polygon points="464,1230 -10,880 -10,960"/>
      <polygon points="464,1230 937,860 937,940"/>
    </svg>

    <header class="brand">
      <span class="brand-mark" aria-hidden="true"></span>
      <h1 class="brand-name">Stellar Step<br>Showcase</h1>
    </header>

    <h2 class="headline headline-year">2017 Regional</h2>
    <h2 class="headline headline-event">Competition</h2>
    <p class="headline headline-season">20th Anniversary Season</p>

    <div class="crowd" role="img" aria-label="Silhouetted crowd of cheering dancers with raised arms along the bottom of the cover"></div>
  </main>
</body>
</html>
```